Brandt Family Motto/Mission Statement

We are creating a poster to be hung in our home with several purpose statements for our family (last name Brandt, and "The Brandt Family" should be included in the poster prominently). The text that we want included is in the attached file.

Our kids range in age from 8 to 17, so we are looking for something that is homey and cheerful, but fairly bold and oriented to older kids (and not so much younger kids).

I've attached a couple of example poster/statements that we generally like. Overall color scheme could include blues and greens and possibly some brown.

Anticipated size of this poster would be 18"x24" with a portrait orientation.

```html
<!DOCTYPE html>
<html lang="en">
<head>
<meta charset="utf-8">
<title>The Brandt Family – Purpose Statements</title>
<link rel="stylesheet" href="https://fonts.googleapis.com/css2?family=Ubuntu:wght@400;500;700&display=swap">
<style>
  :root {
    --page-bg: #ececec;
    --gutter: #1c1c1c;
    --sky: #6cc3ee;
    --azure: #2eaee6;
    --ocean: #0a92d8;
    --cobalt: #0a86cc;
    --deep: #0d63a8;
    --navy: #1b3b86;
    --cyan: #0aa0df;
    --lime: #86c127;
    --ink-navy: #1f3f8a;
    --white: #ffffff;
    --sun: #fff35a;
    --ghost: rgba(255,255,255,0.11);
  }
  * { box-sizing: border-box; margin: 0; padding: 0; }
  html, body { width: 1200px; height: 1000px; overflow: hidden; }
  body {
    background: var(--page-bg);
    font-family: "Ubuntu", "Segoe UI", sans-serif;
    position: relative;
  }
  .poster {
    position: absolute;
    left: 294px; top: 89px;
    width: 606px; height: 819px;
    background: var(--gutter);
    overflow: hidden;
  }
  .panel { position: absolute; overflow: hidden; }
  .panel--learn     { left: 0;     top: 0;     width: 257px; height: 368px; background: var(--sky); }
  .panel--lens      { left: 261px; top: 0;     width: 345px; height: 145px; background: var(--azure); }
  .panel--adventure { left: 261px; top: 149px; width: 345px; height: 219px; background: var(--ocean); }
  .panel--kindness  { left: 0;     top: 372px; width: 359px; height: 173px; background: var(--cobalt); }
  .panel--fit       { left: 363px; top: 372px; width: 243px; height: 173px; background: var(--deep); }
  .panel--right     { left: 0;     top: 549px; width: 242px; height: 270px; background: var(--navy); }
  .panel--humor     { left: 246px; top: 549px; width: 360px; height: 153px; background: var(--cyan); }
  .panel--name      { left: 246px; top: 706px; width: 360px; height: 113px; background: var(--lime);
                      display: flex; align-items: center; justify-content: center; }

  .family-watermark {
    position: absolute;
    left: 4px; top: 70px;
    writing-mode: vertical-lr;
    font-weight: 700;
    font-size: 118px;
    line-height: 0.86;
    color: var(--ghost);
    letter-spacing: 2px;
    pointer-events: none;
    z-index: 2;
  }

  .statement {
    position: absolute;
    color: var(--white);
    font-size: 33px;
    line-height: 34px;
    font-weight: 400;
    white-space: nowrap;
    z-index: 3;
  }
  .statement b { font-weight: 700; }
  .statement--learn { left: 20px; top: 222px; font-size: 40px; line-height: 42px; color: var(--ink-navy); }
  .statement--lens { left: 20px; top: 20px; }
  .statement--adventure { right: 17px; top: 22px; text-align: right; }
  .statement--kindness { left: 76px; top: 38px; font-size: 33px; line-height: 33px; }
  .statement--fit { left: 10px; top: 125px; top: 126px; }
  .statement--fit { top: 126px; }
  .statement--fit { left: 8px; top: 126px; }
  .statement--fit { left: 8px; top: 126px; width: 132px; }
  .statement--right { left: 24px; top: 116px; word-spacing: 3px; line-height: 34px; }
  .statement--humor { left: 19px; top: 27px; font-size: 31px; line-height: 33px; }

  .icon { position: absolute; z-index: 3; }
  .icon--book { left: 14px; top: 111px; width: 124px; height: 95px; }
  .icon--eye { left: 257px; top: 40px; width: 90px; height: 62px; }
  .icon--candle { left: 16px; top: 34px; width: 40px; height: 106px; }

  .art { position: absolute; z-index: 3; border-radius: 8px; }
  .art--snowboarder { left: 37px; top: 52px; width: 103px; height: 115px;
    background: radial-gradient(circle, rgba(255,255,255,0.85), rgba(255,255,255,0.35)); }
  .art--lifter { left: 146px; top: 29px; width: 80px; height: 110px;
    background: radial-gradient(circle, rgba(255,255,255,0.8), rgba(255,255,255,0.3)); }
  .art--thumb { left: 86px; top: 30px; width: 60px; height: 72px;
    background: radial-gradient(circle, rgba(255,255,255,0.8), rgba(255,255,255,0.3)); }
  .art--smile { left: 280px; top: 52px; width: 56px; height: 56px; border-radius: 50%;
    border: 3px solid var(--white); background: rgba(255,255,255,0.15); }

  .family-name {
    font-weight: 700;
    font-size: 36px;
    color: var(--sun);
    white-space: nowrap;
  }
</style>
</head>
<body>
  <main class="poster" aria-label="The Brandt Family purpose statements poster">
    <section class="panel panel--learn">
      <svg class="icon icon--book" viewBox="0 0 124 95" fill="none" stroke="#fff" stroke-width="3" stroke-linejoin="round">
        <path d="M62 20 C45 6 22 4 8 8 L8 80 C24 76 45 78 62 90 C79 78 100 76 116 80 L116 8 C102 4 79 6 62 20 Z"/>
        <path d="M62 20 L62 90"/>
        <path d="M2 14 L2 88 C24 84 45 86 62 94 C79 86 100 84 122 88 L122 14"/>
      </svg>
      <p class="statement statement--learn">We <b>love</b><br>to learn<br>new things.</p>
    </section>

    <section class="panel panel--lens">
      <p class="statement statement--lens">We look at life<br>through<br>a <b>positive</b> lens.</p>
      <svg class="icon icon--eye" viewBox="0 0 90 62" fill="none" stroke="#fff" stroke-width="6">
        <path d="M3 31 C20 6 70 6 87 31 C70 56 20 56 3 31 Z"/>
        <circle cx="45" cy="31" r="14"/>
        <circle cx="45" cy="31" r="5" fill="#fff"/>
      </svg>
    </section>

    <section class="panel panel--adventure">
      <div class="art art--snowboarder" role="img" aria-label="White silhouette of a snowboarder mid-jump"></div>
      <p class="statement statement--adventure">We create<br><b>adventure</b><br>and choose<br>experiences<br>over things.</p>
    </section>

    <section class="panel panel--kindness">
      <svg class="icon icon--candle" viewBox="0 0 40 106" fill="none" stroke="#fff" stroke-width="3">
        <path d="M20 4 C12 16 8 24 12 30 C15 35 25 35 28 30 C32 24 28 16 20 4 Z"/>
        <path d="M20 36 L20 46"/>
        <rect x="2" y="46" width="36" height="58" rx="6"/>
      </svg>
      <p class="statement statement--kindness"><b>Kindness</b><br>guides our words<br>and deeds.</p>
    </section>

    <section class="panel panel--fit">
      <p class="statement statement--fit-text" style="left:10px;top:36px;width:132px;text-align:center;font-size:30px;line-height:33px;">We<br>commit<br>to be <b>fit.</b></p>
      <div class="art art--lifter" role="img" aria-label="White figure lifting a barbell overhead"></div>
    </section>

    <section class="panel panel--right">
      <div class="art art--thumb" role="img" aria-label="Thumbs-up hand outline"></div>
      <p class="statement statement--right">We <b>do what<br>is right</b> even<br>when no one<br>is watching.</p>
    </section>

    <section class="panel panel--humor">
      <p class="statement statement--humor">Our days are<br>brightened by a<br><b>sense of humor.</b></p>
      <div class="art art--smile" role="img" aria-label="Smiling face icon"></div>
    </section>

    <section class="panel panel--name">
      <h1 class="family-name">The Brandt Family</h1>
    </section>

    <div class="family-watermark" aria-hidden="true">THE<br>BRANDT<br>FAMILY</div>
  </main>
</body>
</html>
```